DL Flyer Lantern Creek Hotel Thursday Night Bonus

We require a DL Portrait and landscape flyer for our Thursday Night Bonus Pull.
The way the draw works you must be part of our loyalty program, and on a Thursday night anytime between 5pm and 7pm, a name/number will be picked at random. If that person is in the hotel at the time they will win the jackpot.

The jackpot starts at $250 and goes up by $50 each week, if not won.

The things that the flyer must state:-
* loyalty program members only
* drawn on a Thursday night anytime between 5pm and 7pm
* QMRV/58/46271 must be written somewhere.
* see staff for details.
* our logo

Would like the flyer to be catch peoples attention but remain professional

If your unable to download logo, please forward email address and I will send it throuh

```html
<!DOCTYPE html>
<html lang="en">
<head>
<meta charset="utf-8">
<title>Lantern Creek Hotel – Loyalty Program</title>
<link rel="stylesheet" href="https://fonts.googleapis.com/css2?family=Cinzel:wght@400&family=Marcellus&display=swap">
<style>
  :root {
    --bg: #000000;
    --gold: #f5a623;
    --gold-deep: #8a5a16;
    --gold-mid: #d8952a;
    --white: #ffffff;
    --cash-green: #8f9c7a;
    --cash-light: #d9dcc8;
    --coin: #d9a521;
  }
  * { margin: 0; padding: 0; box-sizing: border-box; }
  html, body { width: 1200px; height: 615px; overflow: hidden; background: var(--bg); }
  .flyer {
    position: relative;
    width: 1200px;
    height: 615px;
    background: var(--bg);
    font-family: "Marcellus", serif;
    color: var(--white);
  }
  .headline {
    position: absolute;
    left: 60px;
    top: 46px;
    font-family: "Cinzel", serif;
    font-weight: 400;
    color: var(--gold);
    font-size: 77px;
    line-height: 90px;
    letter-spacing: 1px;
  }
  .members-only {
    position: absolute;
    left: 64px;
    top: 234px;
    font-size: 34px;
    font-weight: 400;
  }
  .flourish-area {
    position: absolute;
    left: 64px;
    top: 288px;
    width: 476px;
    height: 48px;
    border-radius: 24px 24px 24px 4px;
    background: linear-gradient(90deg, rgba(138,90,22,0.55) 0%, var(--gold-mid) 60%, rgba(240,181,72,0.7) 100%);
  }
  .draw-name {
    position: absolute;
    left: 60px;
    top: 392px;
    width: 286px;
    text-align: center;
    font-size: 32px;
    font-weight: 400;
    line-height: 38px;
  }
  .divider {
    position: absolute;
    left: 356px;
    top: 392px;
    width: 1px;
    height: 74px;
    background: var(--white);
  }
  .draw-times {
    position: absolute;
    left: 387px;
    top: 392px;
    font-size: 22px;
    line-height: 33px;
  }
  .footer-line {
    position: absolute;
    left: 98px;
    top: 529px;
    font-size: 21px;
    word-spacing: 2px;
  }
  .footer-line .sep { margin: 0 18px; }
  .brand {
    position: absolute;
    left: 640px;
    top: 58px;
    display: flex;
    align-items: center;
    gap: 18px;
  }
  .brand-dot {
    width: 46px;
    height: 46px;
    border-radius: 50%;
    background: var(--gold);
  }
  .brand-name {
    font-size: 44px;
    color: var(--white);
    letter-spacing: 1px;
  }
  .cash-artwork {
    position: absolute;
    left: 590px;
    top: 210px;
    width: 610px;
    height: 365px;
    border-radius: 30px 0 0 30px;
    background: radial-gradient(ellipse at 60% 45%, var(--cash-light) 0%, var(--cash-green) 45%, var(--coin) 80%, rgba(0,0,0,0) 100%);
  }
</style>
</head>
<body>
  <main class="flyer">
    <h1 class="headline">LOYALTY<br>PROGRAM</h1>
    <p class="members-only">for members only</p>
    <div class="flourish-area" role="img" aria-label="Gold decorative flourish"></div>

    <h2 class="draw-name">Thursday Night<br>Bonus Pull</h2>
    <span class="divider" aria-hidden="true"></span>
    <p class="draw-times">5pm-7pm<br>starts $250</p>

    <p class="footer-line">QMRV/58/46271<span class="sep">|</span>see staff for details</p>

    <div class="brand">
      <span class="brand-dot" aria-hidden="true"></span>
      <span class="brand-name">Lantern Creek Hotel</span>
    </div>

    <div class="cash-artwork" role="img" aria-label="Stacks of banknotes and gold coins"></div>
  </main>
</body>
</html>
```